Harbor SkyCare Global Air Ambulance Services
Harbor SkyCare Business Package
Harbor SkyCare Global Air Ambulance Services - Aerospace
Creative Brief
Professional
Mr. Doug Wilson Pratt
President / CEO
5273 West Dunmore Suite 410 Scottsdale, Arizona 85312-4706 United States of America
dpratt@harborskycare.example
http://www.harborskycare.example
jaxter42 jaxter42
Congratulations Morlund
vimal8marks vimal8marks
CH pls post feedback
HarborSkyCare HarborSkyCare
Looking away from any vertical formated cards
#191 - #194 - These pieces would be much more desirable if they were closer to our corporate colors: Again, please visit our website for reference: harborskycare.example
SiteAdmin SiteAdmin
Draft #160 by pario is a derivative of #119 by Tovesk, therefore has been taken down.
Draft #144 and its variation by bworkshopz are derivative of #119 by Tovesk, therefore have been taken down.
KDM27 KDM27
I was looking at your address and noticed I live about 5 minutes from there.... what a coincidence!
nanoGlyph nanoGlyph
please comment on my entry #129 and #131 thanks for your time nanoglyph
We love the punch out on #119
tinyrupa tinyrupa
wow alot of contestants, hehe.. i'm joining too in this project
minhcocoa minhcocoa
Thank you! Great comments!
First I want to begin by saying, “Thank you to everyone for participating”. Any ideas that we express are not meant to criticize or critique any designer(s). We simply want to allow you the ability to create “that piece that is just right” for our organization. 1.) I am not sure if maybe our in house design team has made the logo a little darker than the version I have uploaded: However, in order to get a good feeling of the corporate color, please visit our website; harborskycare.example: a. A good representation of what color we are looking for: #2 – The card in the upper right hand corner: On that card, we very much like the fade (bringing in more shadow towards the top ascending). b. Further, we also like the back of that card: 2.) The yellow / gold is too much & not what we are looking for: 3.) Many of the cards look like an “Insurance Identification Card”. 4.) #43 – We really like the drop shadow of the aircraft in the background: It also appears that there is a globe that is slightly visible – This looks very classy & exudes a first class service (This is image we are really trying to capture). 5.) #42 – We really like the shadow of the main portion of the logo 6.) #47 – The logo’s are all wrong: However, on what this person is portraying as the back of the card, the picture of the aircraft is sort of neat. The front of the card has WAY to much going on: 7.) We are most likely going to go with the rounded corners 8.) We are really liking the pictures on the card: Specifically, #57 & #58 captured our eye (with the picture positioning). 9.) We are looking for something that is very different from most business cards: We don’t want the same image for our organization 10.) Review our website for our companies colors: However, please don’t create anything that resembles “The sun burst” on the home page in the upper right hand corner (encompasses the words “Steady Wing Pledge”): We are not a fan of that any longer (I wasn’t a fan of that to begin with). I hope that some of this feedback will help everyone with a little better direction. Again, please understand that we are not trying to critique anyone (everyone has different tastes & we recognize that). Thank you for you for all of your efforts.

```html
<!DOCTYPE html>
<html lang="en">
<head>
<meta charset="utf-8">
<title>Harbor SkyCare Stationery Set</title>
<link href="https://fonts.googleapis.com/css2?family=Montserrat:wght@700&family=Open+Sans:wght@400;600&display=swap" rel="stylesheet">
<style>
  :root {
    --backdrop-light: #d3cfc7;
    --backdrop-dark: #aca69c;
    --maroon: #6a1424;
    --maroon-deep: #3c0812;
    --maroon-mid: #55101d;
    --gold: #e2a31f;
    --gold-light: #f4c85a;
    --paper: #ffffff;
    --paper-shade: #ece9e6;
    --ink: #5a5552;
    --cloud: #d6d3d0;
  }
  * { box-sizing: border-box; margin: 0; padding: 0; }
  html, body { width: 1200px; height: 871px; overflow: hidden; }
  body {
    position: relative;
    background: radial-gradient(ellipse at 50% 40%, var(--backdrop-light), var(--backdrop-dark));
    font-family: "Open Sans", Arial, sans-serif;
    color: var(--ink);
  }
  .piece { position: absolute; overflow: hidden; box-shadow: 4px 6px 10px rgba(0,0,0,.35); }
  .piece svg.art { position: absolute; inset: 0; width: 100%; height: 100%; }

  .brand { position: absolute; display: flex; align-items: center; gap: 6px; }
  .brand-dot { width: 10px; height: 10px; border-radius: 50%; background: currentColor; }
  .brand-name { font-family: "Montserrat", Arial, sans-serif; font-weight: 700; line-height: 1; }
  .brand-tag { position: absolute; font-size: 5px; font-weight: 600; letter-spacing: .8px; text-transform: uppercase; }

  /* Letterhead */
  .letterhead { left: 113px; top: 108px; width: 451px; height: 600px; background: linear-gradient(180deg, var(--paper) 55%, var(--paper-shade)); }
  .letterhead .brand { left: 26px; top: 24px; color: var(--maroon); }
  .letterhead .brand-name { font-size: 17px; }
  .letterhead .brand-tag { left: 42px; top: 44px; color: var(--ink); }
  .letterhead .address { position: absolute; left: 26px; top: 56px; font-size: 5.5px; line-height: 1.5; }
  .letterhead .sky { position: absolute; left: 0; top: 430px; width: 100%; height: 170px;
    background: linear-gradient(180deg, rgba(214,211,208,0), var(--cloud) 60%, #c4bfba); }

  /* Envelope front */
  .envelope-front { left: 600px; top: 108px; width: 492px; height: 204px;
    background: linear-gradient(180deg, var(--maroon-deep), var(--maroon) 60%, var(--maroon-mid)); }
  .envelope-front .brand { left: 18px; top: 18px; color: var(--paper); }
  .envelope-front .brand-name { font-size: 14px; }
  .envelope-front .brand-tag { left: 34px; top: 34px; color: #e6c8cd; font-size: 4.5px; }
  .envelope-front .globe { position: absolute; left: 150px; top: 100px; width: 220px; height: 220px; border-radius: 50%;
    background: radial-gradient(circle at 50% 40%, rgba(255,255,255,.12), rgba(255,255,255,0) 70%); }

  /* Envelope back */
  .envelope-back { left: 600px; top: 360px; width: 492px; height: 204px; background: var(--paper); }
  .envelope-back .seal { position: absolute; left: 238px; top: 120px; width: 16px; height: 16px; border-radius: 50%; background: var(--paper); }

  /* Business card front */
  .card-front { left: 583px; top: 619px; width: 245px; height: 144px; border-radius: 8px;
    background: linear-gradient(180deg, var(--maroon-deep), var(--maroon) 70%); }
  .card-front .brand { left: 38px; top: 50px; color: var(--paper); }
  .card-front .brand-name { font-size: 17px; }
  .card-front .brand-tag { left: 56px; top: 70px; color: #e6c8cd; font-size: 4.5px; }
  .card-front .url { position: absolute; left: 0; right: 0; bottom: 12px; text-align: center; font-size: 5.5px; color: #e6c8cd; }

  /* Business card back */
  .card-back { left: 845px; top: 619px; width: 252px; height: 144px; border-radius: 8px; background: linear-gradient(180deg, var(--paper), var(--paper-shade)); }
  .card-back .brand { left: 10px; top: 14px; color: var(--maroon); }
  .card-back .brand-name { font-size: 11px; }
  .card-back .brand-tag { left: 26px; top: 28px; color: var(--ink); font-size: 3.5px; }
  .card-back .name-band { position: absolute; left: 134px; top: 10px; width: 112px; height: 13px; background: var(--maroon);
    color: var(--paper); font-size: 6.5px; font-weight: 600; padding: 2px 5px; white-space: nowrap; }
  .card-back .title { position: absolute; left: 139px; top: 25px; font-size: 5px; }
  .card-back .details { position: absolute; left: 10px; top: 40px; font-size: 4.6px; line-height: 1.55; }
  .card-back .portrait { position: absolute; left: 118px; top: 52px; width: 40px; height: 56px;
    background: linear-gradient(180deg, #8a8580, #2c2a2c); }
  .card-back .aircraft { position: absolute; left: 196px; top: 46px; width: 46px; height: 20px;
    background: linear-gradient(90deg, rgba(90,85,82,0), rgba(90,85,82,.5)); border-radius: 10px; }
</style>
</head>
<body>

<section class="piece letterhead" aria-label="Letterhead">
  <div class="brand"><span class="brand-dot"></span><span class="brand-name">Harbor SkyCare</span></div>
  <span class="brand-tag">Global Air Ambulance Services</span>
  <p class="address">5273 West Dunmore Suite 410 Scottsdale, Arizona 85312-4706<br>Tel 480.555.0142 Fax 480.555.0143</p>
  <div class="sky" role="img" aria-label="Soft clouds with an aircraft in flight"></div>
  <svg class="art" viewBox="0 0 451 600" preserveAspectRatio="none" aria-hidden="true">
    <path d="M0 600 L0 592 C140 590 300 560 451 470 L451 600 Z" fill="var(--maroon)"/>
    <path d="M40 596 C190 590 330 550 451 462" fill="none" stroke="var(--gold)" stroke-width="4"/>
    <path d="M0 600 C160 596 320 575 451 505 L451 600 Z" fill="var(--maroon-deep)"/>
  </svg>
</section>

<section class="piece envelope-front" aria-label="Envelope front">
  <div class="globe" role="img" aria-label="Faint globe and aircraft trail"></div>
  <svg class="art" viewBox="0 0 492 204" preserveAspectRatio="none" aria-hidden="true">
    <path d="M0 150 C150 195 330 190 492 110" fill="none" stroke="rgba(255,255,255,.18)" stroke-width="2"/>
    <path d="M250 204 C360 190 440 160 492 125" fill="none" stroke="var(--gold)" stroke-width="4"/>
    <path d="M320 204 C400 192 460 170 492 150 L492 204 Z" fill="var(--maroon-deep)"/>
  </svg>
  <div class="brand"><span class="brand-dot"></span><span class="brand-name">Harbor SkyCare</span></div>
  <span class="brand-tag">Global Air Ambulance Services</span>
</section>

<section class="piece envelope-back" aria-label="Envelope back">
  <svg class="art" viewBox="0 0 492 204" preserveAspectRatio="none" aria-hidden="true">
    <defs>
      <linearGradient id="flap" x1="0" y1="0" x2="0" y2="1">
        <stop offset="0" stop-color="var(--maroon-deep)"/>
        <stop offset="1" stop-color="var(--maroon)"/>
      </linearGradient>
    </defs>
    <path d="M0 0 H492 V40 L260 150 Q246 156 232 150 L0 40 Z" fill="url(#flap)"/>
  </svg>
  <span class="seal"></span>
</section>

<section class="piece card-front" aria-label="Business card front">
  <svg class="art" viewBox="0 0 245 144" preserveAspectRatio="none" aria-hidden="true">
    <path d="M0 110 C90 140 180 130 245 95" fill="none" stroke="rgba(255,255,255,.15)" stroke-width="1.5"/>
  </svg>
  <div class="brand"><span class="brand-dot"></span><span class="brand-name">Harbor SkyCare</span></div>
  <span class="brand-tag">Global Air Ambulance Services</span>
  <p class="url">http://www.harborskycare.example</p>
</section>

<section class="piece card-back" aria-label="Business card back">
  <div class="aircraft" role="img" aria-label="Aircraft in flight"></div>
  <svg class="art" viewBox="0 0 252 144" preserveAspectRatio="none" aria-hidden="true">
    <path d="M0 144 L0 138 C90 140 180 125 252 92 L252 144 Z" fill="var(--maroon)"/>
    <path d="M30 142 C120 138 200 118 252 86" fill="none" stroke="var(--gold)" stroke-width="2.5"/>
  </svg>
  <div class="brand"><span class="brand-dot"></span><span class="brand-name">Harbor SkyCare</span></div>
  <span class="brand-tag">Global Air Ambulance Services</span>
  <div class="name-band">Mr. Doug Wilson Pratt</div>
  <p class="title">President / CEO</p>
  <p class="details">5273 West Dunmore Suite 410<br>Scottsdale, Arizona 85312-4706<br>United States of America<br>Office 480.555.0142<br>Cell 480.555.0198<br>Fax 480.555.0143<br>dpratt@harborskycare.example</p>
  <div class="portrait" role="img" aria-label="Portrait photograph of the president"></div>
</section>

</body>
</html>
```